Short term Rentals Marketing agency needs Web design.

We Need a web design for our new company based in Calgary, AB. We are a International Luxury home sharing company (short term rental properties, Villas, Boutique Hotels, Bed & Breakfast, Realtors, Mortgage Brokers). We would like to see designs that look simple, modern and professional. Colors would be bold (red, black, white). The final design should communicate something welcoming, symbolize innovation, and growth. Our goal is to form partnerships with Real Estate, Property Management, Short term Rental Clients to make their lives easier and increase revenue. Vlto Harbor Co. offers a flexible and secure way to market our clients properties while maintaining client satisfaction and amazing customer service. We like how https://brinkleafpromo.ca/ is interactive (when you scroll down, text gets larger). Other similar websites for Short Term Rentals is https://www.quillnestgroup.com/, https://dwelvaroo.com/, https://www.kipmarsh.com/, https://www.tarnpenny.com/about-us/, https://vantrelstays.com. We have attached our Logo.

Target Market(s)

short term rental properties, Villas, Boutique Hotels, Bed & Breakfast, Realtors, Mortgage Brokers, property owners

Industry/Entity Type

Real Estate

Coding

Coded - Design and coding required

Number of Pages Required

5+ page

Font styles to use
Sans Serif

Requirements
Must have
• Home Page, About Us page, How it works, Services, Contact us.

We like how https://brinkleafpromo.ca/ is interactive (when you scroll down, text gets larger).

We have attached our Webcopy. We would like Call to Action Buttons where they're located in the copy and page.

Must have our Logo Colors.

Other similar websites for Short Term Rentals is https://www.quillnestgroup.com/, https://dwelvaroo.com/, https://www.kipmarsh.com/, https://www.tarnpenny.com/about-us/, https://vantrelstays.com.
Nice to have
• Catchy, Interactive Home page.

Should not have
• Should not be too cluttered

```html
<!DOCTYPE html>
<html lang="en">
<head>
<meta charset="utf-8">
<title>Vlto Harbor Co. — Partner with Us</title>
<link href="https://fonts.googleapis.com/css2?family=Montserrat:wght@500;600;700&family=Roboto:wght@400;500;700&display=swap" rel="stylesheet">
<style>
:root{
  --red:#e31e2d;
  --red-dark:#c81522;
  --ink:#1d1d1d;
  --text:#666;
  --soft:#f5f5f5;
  --line:#e4e4e4;
  --white:#fff;
}
*{box-sizing:border-box;margin:0;padding:0}
html,body{width:1200px;height:5190px;overflow:hidden}
body{font-family:"Roboto",sans-serif;color:var(--ink);background:var(--white)}
.wrap{width:980px;margin:0 auto;position:relative}
.eyebrow{font-family:"Montserrat",sans-serif;font-size:15px;letter-spacing:3px;color:#333;font-weight:500}
.title{font-family:"Montserrat",sans-serif;font-weight:600;color:var(--red);font-size:36px;line-height:1.1;text-transform:uppercase}
.center{text-align:center}
.btn{display:inline-block;font-family:"Montserrat",sans-serif;font-weight:600;font-size:14px;text-transform:uppercase;padding:0 28px;height:45px;line-height:45px;text-decoration:none}
.btn-solid{background:var(--red);color:var(--white)}
.btn-outline{border:1.5px solid var(--red);color:var(--red);background:var(--white)}
.copy{font-size:12.5px;line-height:26px;color:var(--text);text-align:justify}

/* hero */
.hero{height:605px;position:relative;overflow:hidden;background:linear-gradient(100deg,#d9d6d2 0%,#ece9e6 35%,#c9c2bb 65%,#8f8882 100%)}
.hero-photo{position:absolute;inset:0;background:linear-gradient(180deg,rgba(255,255,255,.15),rgba(60,55,50,.25))}
.logo{position:absolute;left:110px;top:18px;display:flex;align-items:center;gap:10px;text-decoration:none}
.logo-mark{width:56px;height:56px;background:var(--red)}
.logo-name{font-family:"Montserrat",sans-serif;font-weight:600;font-size:30px;color:var(--ink);line-height:1;white-space:nowrap}
.nav{position:absolute;right:110px;top:40px;display:flex;gap:36px;list-style:none}
.nav a{font-size:15px;color:var(--ink);text-decoration:none}
.nav a.active{color:var(--red)}
.hero-title{position:absolute;left:110px;top:228px;font-family:"Montserrat",sans-serif;font-weight:600;font-size:72px;color:var(--red);white-space:nowrap}
.hero-sub{position:absolute;left:110px;top:320px;font-family:"Montserrat",sans-serif;font-weight:500;font-size:24px;color:var(--ink)}
.hero .btn{position:absolute;left:110px;top:375px}
.play{position:absolute;left:790px;top:256px}
.arrow{position:absolute;top:277px;width:96px;height:84px;border-radius:50%;background:rgba(255,255,255,.75)}
.arrow.left{left:-48px}.arrow.right{right:-48px}
.arrow svg{position:absolute;top:30px}
.arrow.left svg{right:22px}.arrow.right svg{left:22px}

/* split sections */
.split{position:relative}
.split .frame{position:absolute;left:120px;width:446px;height:373px;box-shadow:-10px 10px 0 var(--red)}
.split .text{position:absolute;left:626px;width:464px}
.split .title{font-size:36px;margin:10px 0 24px}
.welcome{height:550px;background:var(--soft)}
.welcome .frame{top:84px;background:linear-gradient(160deg,#c9a57a,#e9d3b0 40%,#5f95b3 75%,#3b6a86)}
.welcome .text{top:100px}
.welcome .btn{margin-top:26px}

/* benefits */
.benefits{height:780px}
.benefits .eyebrow{padding-top:84px}
.benefits .title{margin-top:10px}
.cards{display:flex;gap:18px;margin-top:36px}
.card{width:315px;height:434px;border:1px solid var(--line);background:var(--white);display:flex;flex-direction:column}
.card-img{height:226px;flex:none}
.card h3{font-family:"Montserrat",sans-serif;font-weight:600;font-size:19px;line-height:30px;padding:16px 14px 6px 14px}
.card p{font-size:12.5px;line-height:26px;color:var(--text);padding:0 14px;text-align:justify;flex:1}
.card .btn{align-self:flex-start;margin:0 0 18px 14px;height:40px;line-height:40px;font-size:13px;padding:0 24px}
.benefits .cta{text-align:center;margin-top:36px}

/* how it works */
.how{height:710px;background:var(--soft)}
.how .eyebrow{padding-top:82px}
.how .title{margin-top:10px}
.how .lead{font-size:13.5px;font-weight:500;line-height:28px;margin-top:18px}
.steps{display:flex;justify-content:space-between;margin-top:38px;position:relative}
.step{width:310px;text-align:center}
.step-icon{width:124px;height:124px;border-radius:50%;background:var(--red);margin:0 auto;position:relative;display:flex;align-items:center;justify-content:center}
.step-num{position:absolute;left:-14px;top:36px;width:38px;height:38px;border-radius:50%;background:#333;border:3px solid var(--white);color:var(--white);font-weight:700;font-size:16px;line-height:32px}
.dash{position:absolute;top:62px;width:168px;border-top:2px dashed var(--red)}
.step h3{font-family:"Montserrat",sans-serif;font-weight:600;font-size:18px;margin-top:24px}
.step p{font-size:12.5px;line-height:26px;color:var(--text);margin-top:10px}
.how .cta{text-align:center;margin-top:30px}

/* about */
.about{height:555px}
.about .frame{top:85px;background:linear-gradient(150deg,#a79a8c,#d8cfc4 45%,#6e7a88 80%)}
.about .text{top:100px}
.features{display:grid;grid-template-columns:210px 220px;row-gap:14px;margin-top:18px}
.feature{display:flex;align-items:center;gap:10px;font-size:13.5px;font-weight:500;white-space:nowrap}
.feature svg{flex:none}
.about .btn{margin-top:22px}

/* services */
.services{height:815px;background:#f8f8f8}
.services .eyebrow{padding-top:90px}
.services .title{margin-top:10px}
.services .lead{font-size:13px;line-height:28px;margin-top:16px;color:#333}
.service-grid{display:grid;grid-template-columns:repeat(3,310px);column-gap:25px;row-gap:40px;margin-top:40px}
.service{text-align:center}
.service svg{display:block;margin:0 auto;height:70px}
.service h3{font-size:15px;font-weight:500;margin-top:10px}
.service p{font-size:12.5px;line-height:28px;color:var(--text);margin-top:10px;text-align:justify;text-align-last:center}

/* contact */
.contact{height:695px;background:linear-gradient(135deg,var(--red) 0%,#dd1f2e 50%,var(--red-dark) 100%);color:var(--white)}
.contact .eyebrow{color:var(--white);padding-top:98px}
.contact .title{color:var(--white);margin-top:10px}
.contact .lead{font-size:13px;font-weight:500;line-height:28px;margin-top:18px}
.form{width:564px;margin:18px auto 0;display:grid;grid-template-columns:1fr 1fr;gap:16px 12px}
.field{height:40px;background:var(--white);color:#444;font-size:12px;padding:0 12px;line-height:40px}
.field.wide{grid-column:1/3}
.field.msg{height:88px}
.submit{grid-column:1/3;justify-self:center;width:136px;height:40px;border:1.5px solid var(--white);color:var(--white);font-family:"Montserrat",sans-serif;font-weight:600;font-size:14px;text-align:center;line-height:38px;margin-top:-2px}

/* footer */
.footer{height:480px;position:relative}
.cols{display:flex;padding-top:96px;height:270px}
.col{padding-right:16px;white-space:nowrap}
.col + .col{border-left:2px solid var(--red);padding-left:36px}
.col h4{font-family:"Montserrat",sans-serif;font-weight:600;font-size:15px;margin-bottom:10px}
.col li{list-style:none;font-size:11.5px;line-height:26px;color:#444;display:flex;gap:6px;align-items:center}
.col li.indent{padding-left:18px}
.foot-logo{display:flex;justify-content:center;align-items:center;gap:10px;margin-top:32px}
.foot-rule{border-top:1px solid var(--line);margin-top:20px}
.copyright{text-align:center;font-size:11.5px;color:#555;margin-top:20px}
</style>
</head>
<body>

<header class="hero">
  <div class="hero-photo" role="img" aria-label="Photo of two smiling guests with luggage arriving in a bright living room"></div>
  <a class="logo" href="#"><span class="logo-mark"></span><span class="logo-name">Vlto Harbor Co.</span></a>
  <ul class="nav">
    <li><a class="active" href="#">Home</a></li>
    <li><a href="#">About Us</a></li>
    <li><a href="#">How it works</a></li>
    <li><a href="#">Services</a></li>
    <li><a href="#">Contact us</a></li>
  </ul>
  <h1 class="hero-title">Partner with Us</h1>
  <p class="hero-sub">&amp; Let’s Start Growing Together!</p>
  <a class="btn btn-solid" href="#">Work with us</a>
  <svg class="play" width="64" height="64" viewBox="0 0 64 64"><circle cx="32" cy="32" r="32" fill="#e31e2d"/><path d="M26 20 L46 32 L26 44Z" fill="#fff"/></svg>
  <span class="arrow left"><svg width="14" height="24" viewBox="0 0 14 24"><path d="M12 2 L2 12 L12 22" fill="none" stroke="#555" stroke-width="2"/></svg></span>
  <span class="arrow right"><svg width="14" height="24" viewBox="0 0 14 24"><path d="M2 2 L12 12 L2 22" fill="none" stroke="#e31e2d" stroke-width="2"/></svg></span>
</header>

<section class="split welcome">
  <div class="frame" role="img" aria-label="Photo of a resort patio with lounge seating beside a pool"></div>
  <div class="text">
    <p class="eyebrow">Vlto Harbor Co.</p>
    <h2 class="title">Welcome to Vlto<br>Harbor Co</h2>
    <p class="copy">Vlto Harbor Co. is here to manage and market your short-term rental properties so you don’t have to. Enjoy peace of mind in knowing your short-term rental properties, vacation homes, villas, hotels, and B&amp;Bs are safe, secure, and profitable – no matter where you are in the world. We will help you market, manage, and capitalize on everything, from your newest bookings to house cleaning and upkeep.</p>
    <a class="btn btn-outline" href="#">Learn more</a>
  </div>
</section>

<section class="benefits">
  <div class="wrap center">
    <p class="eyebrow">Vlto Harbor Co.</p>
    <h2 class="title">Our Benifites</h2>
  </div>
  <div class="wrap cards">
    <article class="card">
      <div class="card-img" role="img" aria-label="Photo of a hand drawing a rising growth line" style="background:linear-gradient(135deg,#5b6a82,#9aa7ba)"></div>
      <h3>Increase Your Revenue</h3>
      <p>Having Vlto Harbor Co. manage and market your rental property lets you benefit from increased revenues without having to put in the hours</p>
      <a class="btn btn-outline" href="#">Learn more</a>
    </article>
    <article class="card">
      <div class="card-img" role="img" aria-label="Photo of a host handing keys to guests at a doorway" style="background:linear-gradient(135deg,#d8d2c8,#8c7f70)"></div>
      <h3>Receive Constant Support</h3>
      <p>Our dedicated team is there to take care of your property so that you don’t have to. Our affordable and professional services include</p>
      <a class="btn btn-outline" href="#">Learn more</a>
    </article>
    <article class="card">
      <div class="card-img" role="img" aria-label="Photo of a small model house held in an open hand" style="background:linear-gradient(135deg,#e9e9e9,#b7b7b7)"></div>
      <h3>Manage Your Risks and Insurance</h3>
      <p>Having Vlto Harbor Co. manage and market your rental property lets you benefit</p>
      <a class="btn btn-outline" href="#">Learn more</a>
    </article>
  </div>
  <div class="cta"><a class="btn btn-solid" href="#">Work with us</a></div>
</section>

<section class="how">
  <div class="wrap center">
    <p class="eyebrow">EASY, FLEXIBLE FAST</p>
    <h2 class="title">How it Works</h2>
    <p class="lead">We try to keep our application, management, and marketing process as quick and simple as possible.<br>To sign up to Vlto Harbor Co, you can follow these three steps:</p>
  </div>
  <div class="wrap steps">
    <span class="dash" style="left:240px"></span>
    <span class="dash" style="left:582px"></span>
    <div class="step">
      <div class="step-icon"><span class="step-num">1.</span>
        <svg width="60" height="60" viewBox="0 0 60 60" fill="none" stroke="#fff" stroke-width="2.5"><circle cx="30" cy="22" r="10"/><path d="M18 22a12 12 0 0 1 24 0"/><path d="M12 54c2-12 10-16 18-16s16 4 18 16"/></svg>
      </div>
      <h3>Book A Consultation</h3>
      <p>Give us a call to set up your own consultation session where we will discuss your needs, goals, and concerns regarding the management and marketing of your short-term rental properties.</p>
    </div>
    <div class="step">
      <div class="step-icon"><span class="step-num">2.</span>
        <svg width="60" height="60" viewBox="0 0 60 60" fill="none" stroke="#fff" stroke-width="2.5"><path d="M8 28 L30 10 L52 28"/><rect x="14" y="26" width="32" height="26"/><rect x="20" y="34" width="8" height="8"/><rect x="32" y="34" width="8" height="18"/></svg>
      </div>
      <h3>Optimize Your Property</h3>
      <p>Once you’ve decided what you would like from your rental property, we will help you make it a reality. This involves optimizing your pricing, listings, operations, bookings, and much more.</p>
    </div>
    <div class="step">
      <div class="step-icon"><span class="step-num">3.</span>
        <svg width="60" height="60" viewBox="0 0 60 60" fill="none" stroke="#fff" stroke-width="2.5"><path d="M14 34 L34 14 L50 12 L48 28 L28 48Z"/><circle cx="41" cy="21" r="3"/><path d="M24 34 l8 -8"/></svg>
      </div>
      <h3>Start Hosting Renters</h3>
      <p>You can start hosting renters in no time thanks to our quick turnaround times and professional services. We will help you maintain your properties for as long as you need us.</p>
    </div>
  </div>
  <div class="cta"><a class="btn btn-solid" href="#">Get started today</a></div>
</section>

<section class="split about">
  <div class="frame" role="img" aria-label="Photo of a couple relaxing on a sofa among moving boxes"></div>
  <div class="text">
    <p class="eyebrow">ABOUT US</p>
    <h2 class="title">Vlto Harbor Co</h2>
    <p class="copy">Vlto Harbor Co. offers you a flexible and secure way to oversee and manage and market your short-term rental properties. We have the skills needed to get our clients the absolute best value for their money, because we give our 110% to each and every one of our valued property owners. Some of the things that set us apart include:</p>
    <div class="features">
      <span class="feature"><svg width="20" height="20" viewBox="0 0 20 20"><circle cx="10" cy="10" r="10" fill="#e31e2d"/><path d="M5 10h9M10 6l4 4-4 4" stroke="#fff" stroke-width="2" fill="none"/></svg>Amazing Customer Service</span>
      <span class="feature"><svg width="20" height="20" viewBox="0 0 20 20"><circle cx="10" cy="10" r="10" fill="#e31e2d"/><path d="M5 10h9M10 6l4 4-4 4" stroke="#fff" stroke-width="2" fill="none"/></svg>Innovation and Creativity</span>
      <span class="feature"><svg width="20" height="20" viewBox="0 0 20 20"><circle cx="10" cy="10" r="10" fill="#e31e2d"/><path d="M5 10h9M10 6l4 4-4 4" stroke="#fff" stroke-width="2" fill="none"/></svg>Knowledge and Skills</span>
    </div>
    <a class="btn btn-outline" href="#">Learn more</a>
  </div>
</section>

<section class="services">
  <div class="wrap center">
    <p class="eyebrow">OUR SERVICES</p>
    <h2 class="title">What We Offer</h2>
    <p class="lead">As an innovative rental management and marketing agency, we don’t just do the bare minimum when it comes to our clients – we go above and beyond what is expected of us. Our friendly and welcoming team of experts is dedicated to meeting every one of your needs and exceeding your expectations.<br>Here are some of our amazing offers:</p>
  </div>
  <div class="wrap service-grid">
    <div class="service">
      <svg viewBox="0 0 70 70" fill="none" stroke="#e31e2d" stroke-width="2"><rect x="6" y="10" width="58" height="24" rx="3"/><path d="M18 16l2 4 4 .5-3 3 1 4-4-2-4 2 1-4-3-3 4-.5z M35 16l2 4 4 .5-3 3 1 4-4-2-4 2 1-4-3-3 4-.5z M52 16l2 4 4 .5-3 3 1 4-4-2-4 2 1-4-3-3 4-.5z"/><path d="M30 40v18M30 40c4 0 6 4 6 8v10"/></svg>
      <h3>Import and Export Auto Ratings</h3>
      <p>You can easily update or change your listings’ prices from one place and automatically import/export those changes to all your other platforms...</p>
    </div>
    <div class="service">
      <svg viewBox="0 0 70 70" fill="none" stroke="#e31e2d" stroke-width="2"><rect x="16" y="4" width="38" height="62"/><rect x="22" y="10" width="26" height="50"/><path d="M30 26v18M26 30l4-4 4 4M40 44V26M36 40l4 4 4-4"/></svg>
      <h3>Direct Bookings</h3>
      <p>You can easily update or change your listings’ prices from one place and automatically import/export those changes to all your other platforms...</p>
    </div>
    <div class="service">
      <svg viewBox="0 0 70 70" fill="none" stroke="#e31e2d" stroke-width="2"><path d="M14 4h32l10 10v52H14z"/><path d="M20 16h18M20 24h24"/><path d="M24 54V44M30 54V38M36 54V46M42 54V34"/></svg>
      <h3>Powerful Reporting</h3>
      <p>Vlto Harbor Co. will boost your revenue by listing your property on different rental platforms for your short-term rental properties...</p>
    </div>
    <div class="service">
      <svg viewBox="0 0 70 70" fill="none" stroke="#e31e2d" stroke-width="2"><rect x="6" y="12" width="46" height="46"/><path d="M6 24h46M16 6v12M42 6v12"/><rect x="12" y="30" width="8" height="8"/><rect x="25" y="30" width="8" height="8"/><rect x="12" y="44" width="8" height="8"/><rect x="25" y="44" width="8" height="8"/><path d="M62 18L40 50l-4 6 6-3 22-32z"/></svg>
      <h3>Cleaning and Organization</h3>
      <p>Keep track of every single transaction date and customer detail, as well as rates and cleaning fees, tax amounts, and more - thanks...</p>
    </div>
    <div class="service">
      <svg viewBox="0 0 70 70" fill="none" stroke="#e31e2d" stroke-width="2"><circle cx="35" cy="26" r="12"/><path d="M21 28v-4a14 14 0 0 1 28 0v4"/><rect x="17" y="24" width="6" height="10" rx="2"/><rect x="47" y="24" width="6" height="10" rx="2"/><path d="M50 34c0 6-6 8-12 8"/><path d="M14 66c2-12 10-18 21-18s19 6 21 18"/></svg>
      <h3>Customer Communication</h3>
      <p>We can manage and oversee any work-orders, set cleaning tasks, and give you real-time updates thanks to our integrated calendar system...</p>
    </div>
    <div class="service">
      <svg viewBox="0 0 70 70" fill="none" stroke="#e31e2d" stroke-width="2"><rect x="8" y="12" width="54" height="50"/><path d="M8 24h54M20 6v12M50 6v12"/><rect x="16" y="32" width="8" height="7"/><rect x="31" y="32" width="8" height="7"/><rect x="46" y="32" width="8" height="7"/><rect x="16" y="46" width="8" height="7"/><rect x="31" y="46" width="8" height="7"/><rect x="46" y="46" width="8" height="7"/></svg>
      <h3>Calendar Adjustments</h3>
      <p>We help you keep an open line of communication with your clients by managing their booking process, sending them check-in instructions...</p>
    </div>
  </div>
</section>

<section class="contact" role="region" aria-label="Contact form over a faint photo of a bright living room">
  <div class="wrap center">
    <p class="eyebrow">GET IN TOUCH</p>
    <h2 class="title">Contact Us Today</h2>
    <p class="lead">If you are interested in letting Vlto Harbor Co. manage and market your short-term rental properties, vacation homes, villas, hotels,<br>and B&amp;Bs contact us today. One of our expert team members will be in touch to start discussing your needs and potential questions.<br>We look forward to working with you!</p>
  </div>
  <div class="form">
    <div class="field">First Name *</div>
    <div class="field">Last Name *</div>
    <div class="field wide">Property Address</div>
    <div class="field">Email Address *</div>
    <div class="field">Phone *</div>
    <div class="field wide msg">Message</div>
    <div class="submit">SUBMIT</div>
  </div>
</section>

<footer class="footer">
  <div class="wrap cols">
    <div class="col" style="width:250px">
      <h4>CONTACT US</h4>
      <ul>
        <li><svg width="12" height="14" viewBox="0 0 12 14"><path d="M6 0a5 5 0 0 1 5 5c0 4-5 9-5 9S1 9 1 5a5 5 0 0 1 5-5z" fill="#e31e2d"/><circle cx="6" cy="5" r="2" fill="#fff"/></svg>48 Larkspur Row, Calgary AB</li>
        <li class="indent">T2P 0K4, Canada</li>
        <li><svg width="12" height="12" viewBox="0 0 12 12"><path d="M2 0l3 3-1.5 2a7 7 0 0 0 3.5 3.5L9 7l3 3-2 2C5 12 0 7 0 2z" fill="#e31e2d"/></svg>403 555 0148</li>
        <li><svg width="12" height="14" viewBox="0 0 12 14"><path d="M6 0a5 5 0 0 1 5 5c0 4-5 9-5 9S1 9 1 5a5 5 0 0 1 5-5z" fill="#e31e2d"/><circle cx="6" cy="5" r="2" fill="#fff"/></svg>info@vltoharborco.com</li>
      </ul>
    </div>
    <div class="col" style="width:192px">
      <h4>OFFICE HOURS</h4>
      <ul><li>9:30am – 5:30pm</li><li>Weekdays</li><li>12:00pm – 4:00pm</li><li>Saturday</li><li>Sunday – Closed</li></ul>
    </div>
    <div class="col" style="width:168px">
      <h4>APARTMENTS</h4>
      <ul><li>One Bedroom</li><li>Two Bedroom</li><li>Three Bedroom</li><li>Duplex Suite</li></ul>
    </div>
    <div class="col" style="width:228px">
      <h4>SERVICES</h4>
      <ul><li>Import and Export Auto Ratings</li><li>Direct Bookings</li><li>Powerful Reporting</li><li>Cleaning and Organization</li><li>Customer Communication</li><li>Calendar Adjustments</li></ul>
    </div>
    <div class="col" style="width:142px;padding-right:0">
      <h4>QUICK LINKS</h4>
      <ul><li>Home</li><li>About Us</li><li>How it works</li><li>Services</li><li>Contact us</li></ul>
    </div>
  </div>
  <div class="wrap">
    <div class="foot-logo"><span class="logo-mark" style="width:48px;height:48px"></span><span class="logo-name">Vlto Harbor Co.</span></div>
    <div class="foot-rule"></div>
    <p class="copyright">Copyright © 2020 Vlto Harbor Co. All Rights Reserved.</p>
  </div>
</footer>

</body>
</html>
```